Company letter head

Hello,
We are a global logistics company requiring a letterhead design for all our company documentation.
Company Name: Clearly display the full name of your company at the top of the letterhead.
Logo: Include your company logo for brand recognition.
Contact Information: This includes your company's address, phone number, email address, and website URL.
Target Market(s)
Clients/customers
Industry/Entity Type
Logistics
Font styles to use
Sans Serif
Requirements
Must have
- Company name and logo
Nice to have
- borders, header/footers

```html
<!DOCTYPE html>
<html lang="en">
<head>
<meta charset="utf-8">
<title>Northway Freight Lines — Letterhead</title>
<link href="https://fonts.googleapis.com/css2?family=Montserrat:wght@400;600;700&family=Open+Sans:wght@400&display=swap" rel="stylesheet">
<style>
  :root {
    --backdrop: #2a2322;
    --paper: #ffffff;
    --ink: #3a3a3a;
    --ink-soft: #555555;
    --brand-red: #e0161e;
    --band-dark: #3d3c3e;
    --footer-text: #f2f2f2;
  }
  * { box-sizing: border-box; margin: 0; padding: 0; }
  html, body {
    width: 1200px; height: 900px; overflow: hidden;
    background: var(--backdrop);
  }
  body { display: flex; align-items: center; justify-content: center; }
  .letterhead {
    position: relative;
    width: 608px; height: 860px;
    background: var(--paper);
    font-family: "Open Sans", sans-serif;
    color: var(--ink);
    overflow: hidden;
    box-shadow: 0 12px 40px rgba(0,0,0,0.45);
  }
  .header {
    display: flex; justify-content: space-between; align-items: flex-start;
    padding: 48px 48px 0 56px;
  }
  .brand {
    display: flex; align-items: center; gap: 10px;
    font-family: "Montserrat", sans-serif;
    font-weight: 700; font-size: 17px; letter-spacing: 0.5px;
    color: var(--ink); text-transform: uppercase;
  }
  .brand-dot {
    width: 26px; height: 26px; border-radius: 50%;
    background: var(--brand-red);
  }
  .contact {
    margin-top: 60px;
    font-family: "Montserrat", sans-serif;
    font-size: 9.5px; line-height: 1.45; color: var(--ink-soft);
  }
  .contact-item { display: flex; align-items: center; gap: 5px; }
  .contact-icon { width: 9px; height: 9px; flex: none; }
  .letter-body {
    padding: 40px 56px 0 56px;
    font-size: 9.5px; line-height: 1.55; color: var(--ink-soft);
  }
  .salutation { margin-bottom: 14px; }
  .letter-body p.paragraph { margin-bottom: 14px; }
  .closing { margin-top: 4px; }
  .signature {
    width: 90px; height: 50px; margin-top: 14px;
    background: linear-gradient(90deg, #f4f4f4, #e9e9e9);
    border-radius: 4px;
  }
  .footer {
    position: absolute; left: 0; right: 0; bottom: 0; height: 150px;
  }
  .footer svg { position: absolute; inset: 0; width: 100%; height: 100%; }
  .footer-name {
    position: absolute; left: 56px; bottom: 40px;
    font-family: "Montserrat", sans-serif; font-size: 12px; font-weight: 600;
    color: var(--footer-text); letter-spacing: 0.3px;
  }
</style>
</head>
<body>
  <main class="letterhead">
    <header class="header">
      <div class="brand"><span class="brand-dot"></span>Northway Freight Lines</div>
      <address class="contact" style="font-style:normal">
        <div>48 Harbour Gate Road,</div>
        <div>Lakefield, ON K0L 2H0</div>
        <div class="contact-item">
          <svg class="contact-icon" viewBox="0 0 10 10"><circle cx="5" cy="5" r="5" fill="var(--brand-red)"/><path d="M3.2 2.6l1 1-0.5 0.7a3.6 3.6 0 0 0 2 2l0.7-0.5 1 1-0.7 0.8c-2 0-4.3-2.3-4.3-4.3z" fill="#fff"/></svg>
          (555)310-2240
        </div>
        <div class="contact-item">
          <svg class="contact-icon" viewBox="0 0 10 10"><circle cx="5" cy="5" r="5" fill="var(--brand-red)"/><rect x="2.4" y="3.2" width="5.2" height="3.6" fill="none" stroke="#fff" stroke-width="0.8"/><path d="M2.4 3.2l2.6 2 2.6-2" fill="none" stroke="#fff" stroke-width="0.8"/></svg>
          hello@northwayfreight.com
        </div>
        <div class="contact-item">
          <svg class="contact-icon" viewBox="0 0 10 10"><circle cx="5" cy="5" r="5" fill="var(--brand-red)"/><circle cx="5" cy="5" r="2.6" fill="none" stroke="#fff" stroke-width="0.7"/><path d="M2.4 5h5.2M5 2.4c-1.2 1.4-1.2 3.8 0 5.2M5 2.4c1.2 1.4 1.2 3.8 0 5.2" fill="none" stroke="#fff" stroke-width="0.6"/></svg>
          www.northwayfreight.com
        </div>
      </address>
    </header>

    <section class="letter-body">
      <p class="salutation">Dear customer,</p>
      <p class="paragraph">Lorem ipsum dolor sit amet, consectetur adipisicing elit, sed do eiusmod tempor incididunt ut labore et dolore magna aliqua. Ut enim ad minim veniam, quis nostrud exercitation ullamco laboris nisi ut aliquip ex ea commodo consequat. Duis aute irure dolor in reprehenderit in voluptate velit esse cillum dolore eu fugiat nulla pariatur. Excepteur sint occaecat cupidatat non proident, sunt in culpa qui officia deserunt mollit anim id est laborum.</p>
      <p class="paragraph">Lorem ipsum dolor sit amet, consectetur adipisicing elit, sed do eiusmod tempor incididunt ut labore et dolore magna aliqua. Ut enim ad minim veniam, quis nostrud exercitation ullamco laboris nisi ut aliquip ex ea commodo consequat. Duis aute irure dolor in reprehenderit in voluptate velit esse cillum dolore eu fugiat nulla pariatur. Excepteur sint occaecat cupidatat non proident, sunt in culpa qui officia deserunt mollit anim id est laborum.</p>
      <p class="paragraph">Lorem ipsum dolor sit amet, consectetur adipisicing elit, sed do eiusmod tempor incididunt ut labore et dolore magna aliqua. Ut enim ad minim veniam, quis nostrud exercitation ullamco laboris nisi ut aliquip ex ea commodo consequat. Duis aute irure dolor in reprehenderit in voluptate velit esse cillum dolore eu fugiat nulla pariatur. Excepteur sint occaecat cupidatat non proident, sunt in culpa qui officia deserunt mollit anim id est laborum.</p>
      <p class="paragraph">Lorem ipsum dolor sit amet, consectetur adipisicing elit, sed do eiusmod tempor incididunt ut labore et dolore magna aliqua. Ut enim ad minim veniam, quis nostrud exercitation ullamco laboris nisi ut aliquip ex ea commodo consequat. Duis aute irure dolor in reprehenderit.</p>
      <p class="closing">Yours Sincerely,</p>
      <div class="signature" role="img" aria-label="Handwritten signature of the sender"></div>
    </section>

    <footer class="footer">
      <svg viewBox="0 0 608 150" preserveAspectRatio="none" aria-hidden="true">
        <path d="M0 40 Q300 80 608 150 L0 150 Z" fill="var(--band-dark)"/>
        <path d="M0 40 Q300 80 608 150" fill="none" stroke="var(--brand-red)" stroke-width="3"/>
      </svg>
      <div class="footer-name">Northway Freight Lines</div>
    </footer>
  </main>
</body>
</html>
```